PowerPoint Template Briefing for VALDRIK

Create a professional, consistent PowerPoint template in 16:9 format that adheres to VALDRIK's corporate identity guidelines. This template will be used regularly for client presentations, project proposals, and internal communications.

Template Requirements
- Format: 16:9 widescreen format for modern display compatibility
- Master slides to include:
- - Title slide with prominent logo placement
- - Section divider slides
- - Content slides with various layouts (text only, text with images, comparison layouts)
- - Data presentation slides (charts, tables, graphs)
- - Quote/testimonial slide
- - Contact/closing slide

Brand Elements Integration
- Logo placement: Consistent positioning on all slides (preferably top left or bottom right)
- Use both logo variations appropriately (text under icon for title slides, text right of icon for content slides)
- Color scheme: Implement the VALDRIK color palette throughout:
- - Primary Dark Gray (#404040) for main text and headers
- - Primary Blue (#295F7C) for accents and highlights
- - Highlight Blue (#3B8AB4) for call-outs and emphasis
- Typography: Montserrat font family exclusively, with appropriate size hierarchy:
- - Slide titles: Montserrat Bold
- - Headings: Montserrat SemiBold
- - Body text: Montserrat Regular
- - Captions/footnotes: Montserrat Light

Design Elements
- Clean, minimalist design with ample white space
- Subtle background elements that evoke global connectivity and time zones
- Modern, professional look aligned with IT industry standards
- Consistent footer with slide numbers and optional space for confidentiality notices
- Custom bullet points and dividers using brand colors

Technical Specifications
- Compatible with PowerPoint 2016 and newer versions
- Embedded Montserrat font or fallback instructions
- Editable text boxes and image placeholders
- Properly set up slide masters and layouts
- Optimized file size for easy sharing

Deliverables
- .POTX template file
- Brief usage guidelines for the template
- Sample slides demonstrating various layouts and proper usage

This template should serve as the foundation for all VALDRIK presentations, ensuring brand consistency while providing flexibility for various content needs.undefined

```html
<!DOCTYPE html>
<html lang="en">
<head>
<meta charset="utf-8">
<title>VALDRIK Presentation Template</title>
<link href="https://fonts.googleapis.com/css2?family=Montserrat:wght@300;400;500;600;700&family=Lato:wght@400;700;900&display=swap" rel="stylesheet">
<style>
:root{
  --canvas:#b0b1b6;
  --white:#ffffff;
  --navy:#23506f;
  --blue:#295f7c;
  --blue-deep:#1e4560;
  --ink:#2f2f2f;
  --text:#404040;
  --gold:#a8894f;
}
*{margin:0;padding:0;box-sizing:border-box}
html,body{width:1025px;height:1200px;overflow:hidden;background:var(--canvas)}
body{position:relative;font-family:"Montserrat",sans-serif;color:var(--text)}
.slide{position:absolute;width:437px;height:246px;background:var(--white);overflow:hidden}
.brand{position:absolute;font-family:"Montserrat",sans-serif;font-weight:500;color:var(--navy);letter-spacing:.5px;line-height:1;white-space:nowrap}
.photo{position:absolute}

/* cover */
.s-cover{left:65px;top:49px}
.s-cover .brand{left:20px;top:61px;font-size:16px}
.cover-title{position:absolute;left:18px;top:100px;font-weight:700;font-size:19px;line-height:28.5px;color:var(--ink)}
.cover-title .accent{color:var(--navy)}
.cover-name{position:absolute;left:225px;top:108px;width:200px;text-align:center;font-weight:500;font-size:30px;color:var(--navy);letter-spacing:1px;line-height:1}

/* section divider */
.s-divider{left:535px;top:52px;background:linear-gradient(135deg,#2d6585 0%,#295f7c 45%,#1f4a66 100%)}
.divider-mark{position:absolute;left:0;right:0;top:62px;text-align:center;font-weight:500;font-size:14px;color:var(--white);letter-spacing:1px}
.divider-rule{position:absolute;left:136px;width:164px;height:1.5px;background:var(--white)}
.divider-title{position:absolute;left:0;right:0;top:150px;text-align:center;font-family:"Lato",sans-serif;font-weight:900;font-size:30px;color:var(--white);letter-spacing:.5px}

/* about */
.s-about{left:65px;top:325px}
.s-about .brand{left:14px;top:14px;font-size:16px}
.about-tab{position:absolute;left:211px;top:0;width:226px;height:37px;background:var(--navy);color:var(--white);font-weight:700;font-size:13px;padding:11px 0 0 15px}
.about-photo{left:3.5px;top:47.5px;width:209px;height:195px;background:linear-gradient(160deg,#6d6a63 0%,#a39b8e 50%,#d9d4cc 100%)}
.about-copy{position:absolute;left:225px;top:55px;width:198px;font-size:5.8px;line-height:9.1px;color:#333}
.about-list{position:absolute;left:225px;top:141px;list-style:none;font-size:5.8px;color:#333}
.about-list li{position:relative;padding-left:10px;height:17.2px}
.about-list li::before{content:"";position:absolute;left:0;top:1.5px;width:4.5px;height:4.5px;border-radius:50%;background:var(--navy)}

/* solutions */
.s-solutions{left:535px;top:328px}
.s-solutions .brand{left:12px;top:12px;font-size:12px}
.head-divider{position:absolute;width:1px;background:#555}
.s-solutions .head-divider{left:101px;top:7px;height:20px}
.head-title{position:absolute;font-weight:700;color:var(--ink)}
.s-solutions .head-title{left:115px;top:11px;font-size:12px}
.sol-band{position:absolute;left:0;top:35px;width:437px;height:132px;background:var(--blue-deep)}
.sol-card{position:absolute;top:53px;width:136px;height:175px;background:var(--white);box-shadow:0 1px 3px rgba(0,0,0,.12)}
.sol-card .photo{left:0;top:0;width:136px;height:93px}
.sol-card h3{position:absolute;left:0;right:0;top:104px;text-align:center;font-weight:600;font-size:8px;color:var(--ink);letter-spacing:.2px}
.sol-card p{position:absolute;left:18px;right:18px;top:121px;text-align:center;font-size:5.3px;line-height:7.8px;color:#444}
.tone-1{background:linear-gradient(135deg,#0c2b4a 0%,#1f6aa0 50%,#0d2238 100%)}
.tone-2{background:linear-gradient(135deg,#28323c 0%,#5b6470 50%,#2c3a48 100%)}
.tone-3{background:linear-gradient(135deg,#1b2c42 0%,#47607c 50%,#9ab0c6 100%)}

/* contents */
.s-contents{left:65px;top:604px}
.s-contents .brand{left:18px;top:19px;font-size:15px}
.s-contents .head-title{left:134px;top:14px;font-size:10.5px;line-height:12px}
.toc{position:absolute;left:16px;top:62px;width:163px;list-style:none}
.toc li{display:flex;align-items:center;border-bottom:0.7px solid #8a8a8a;font-weight:500;font-size:7.8px;color:var(--ink);line-height:9.6px}
.toc li span{width:23px;padding-left:9px}
.toc .two{height:32px}
.toc .one{height:20.5px}
.toc li:last-child{border-bottom:none}
.contents-art{position:absolute;left:0;top:0}

/* three-column */
.s-columns{left:538px;top:604px}
.s-columns .brand{left:16px;top:23px;font-size:17px}
.s-columns .head-divider{left:134px;top:18px;height:27px}
.s-columns .head-title{left:151px;top:19px;font-size:11.5px;line-height:13.5px}
.col{position:absolute;top:68px;width:128px}
.col .photo{left:0;top:0;width:128px;height:89px}
.col h3{position:absolute;top:104px;left:0;width:132px;font-weight:700;font-size:8px;line-height:9.8px;color:var(--ink)}
.col p{position:absolute;top:128px;left:1px;width:120px;font-size:5.9px;line-height:8.2px;color:#333}
.tone-4{background:linear-gradient(135deg,#c9c4bc 0%,#7c7f86 50%,#eae7e2 100%)}
.tone-5{background:linear-gradient(135deg,#e9e8e6 0%,#8e8a84 50%,#3d4a44 100%)}
.tone-6{background:linear-gradient(135deg,#dcdedf 0%,#8b6e58 50%,#4a5860 100%)}

/* chart */
.s-chart{left:70px;top:888px}
.s-chart .brand{left:16px;top:19px;font-size:16px}
.chart-art{position:absolute;left:0;top:0}
.chart-panel{position:absolute;left:316px;top:0;width:121px;height:246px;background:var(--navy);padding:21px 0 0 16px;color:var(--white)}
.chart-panel h2{font-weight:700;font-size:8.6px;line-height:11px}
.chart-panel p{margin-top:9px;width:96px;font-family:"Lato",sans-serif;font-weight:400;font-size:5.6px;line-height:8.65px}

/* closing */
.s-close{left:543px;top:891px;background:linear-gradient(135deg,#2b6384 0%,#295f7c 50%,#214f6b 100%)}
.close-rule{position:absolute;left:145px;width:148px;height:1.5px;background:var(--white)}
.close-title{position:absolute;left:0;right:0;top:113px;text-align:center;font-family:"Lato",sans-serif;font-weight:900;font-size:25px;color:var(--white)}
.contact{position:absolute;top:202px;display:flex;align-items:center;gap:6px;color:var(--white);font-family:"Lato",sans-serif;font-size:6.9px;line-height:9.5px}
.contact .icon{width:15px;height:15px;border-radius:50%;background:#2a2f35;display:flex;align-items:center;justify-content:center}
</style>
</head>
<body>

<section class="slide s-cover">
  <div class="brand">VALDRIK</div>
  <h1 class="cover-title">
    <span class="accent">SMART IT</span><br>
    <span class="accent">OUTSOURCING</span><br>
    &amp; SCALABLE<br>
    BUSINESS GROWTH
  </h1>
  <div class="cover-name">VALDRIK</div>
</section>

<section class="slide s-divider">
  <div class="photo" role="img" aria-label="Office team at computers, tinted blue" style="inset:0;background:radial-gradient(ellipse at 70% 60%,rgba(20,50,70,.45),rgba(0,0,0,0) 70%)"></div>
  <div class="divider-mark">VALDRIK</div>
  <div class="divider-rule" style="top:137px"></div>
  <h2 class="divider-title">ABOUT US</h2>
  <div class="divider-rule" style="top:202px"></div>
</section>

<section class="slide s-about">
  <div class="brand">VALDRIK</div>
  <div class="about-tab">ABOUT US</div>
  <div class="photo about-photo" role="img" aria-label="Businesswoman working on a laptop in an office"></div>
  <p class="about-copy">Sed ut perspiciatis unde omnis iste natus error sit voluptatem accusantium doloremque laudantium, totam rem aperiam, eaque ipsa quae ab illo inventore veritatis et quasi architecto beatae vitae dicta sunt explicabo. Nemo enim ipsam voluptatem quia voluptas sit aspernatur aut odit aut fugit, sed quia consequuntur magni dolores eos qui ratione voluptatem sequi nesciunt. Neque porro quisquam est, qui dolorem ipsum quia dolor sit amet, consectetur, adipisci</p>
  <ul class="about-list">
    <li>Lorem ipsum dolor sit amet, consectetur adipiscing elit.</li>
    <li>Phasellus eu nisl sit amet purus suscipit dapibus.</li>
    <li>Nullam nec nulla a eros elementum iaculis.</li>
    <li>Praesent eget enim pretium, dignissim massa</li>
    <li>Ut tincidunt elit eu mauris varius tristique.</li>
  </ul>
</section>

<section class="slide s-solutions">
  <div class="brand">VALDRIK</div>
  <div class="head-divider"></div>
  <h2 class="head-title">Solutions</h2>
  <div class="sol-band"></div>
  <article class="sol-card" style="left:9px">
    <div class="photo tone-1" role="img" aria-label="Digital globe interface with a consultant"></div>
    <h3>EXPERT MATCHING</h3>
    <p>Find the right IT freelancer for your project—fast and hassle-free. We connect you with top-tier experts worldwide, ensuring seamless integration and high-quality results.</p>
  </article>
  <article class="sol-card" style="left:151px">
    <div class="photo tone-2" role="img" aria-label="Team on a video conference wall"></div>
    <h3>SOLUTION ORCHESTRATION</h3>
    <p>Need a complete IT team? We assemble and manage expert teams by combining specialized freelancers and service providers into a cohesive, high-performing unit.</p>
  </article>
  <article class="sol-card" style="left:293px">
    <div class="photo tone-3" role="img" aria-label="Agile, Scrum and Kanban dashboard display"></div>
    <h3>IT CONSULTING</h3>
    <p>Optimize your IT strategy with our expert guidance. From agile transformation to ITSM implementation, we help businesses innovate and scale efficiently.</p>
  </article>
</section>

<section class="slide s-contents">
  <svg class="contents-art" width="437" height="246" viewBox="0 0 437 246">
    <path d="M269 0 Q168 123 292 246 L437 246 L437 0 Z" fill="#23506f"/>
    <defs>
      <linearGradient id="tocPhoto" x1="0" y1="0" x2="1" y2="1">
        <stop offset="0" stop-color="#3c4a44"/>
        <stop offset=".55" stop-color="#5a7391"/>
        <stop offset="1" stop-color="#cfd3d6"/>
      </linearGradient>
    </defs>
    <g role="img" aria-label="Smiling man taking notes at a laptop">
      <path d="M285 0 Q190 123 305 246 L437 246 L437 0 Z" fill="url(#tocPhoto)"/>
    </g>
  </svg>
  <div class="brand">VALDRIK</div>
  <h2 class="head-title">Table of<br>Contents</h2>
  <ol class="toc">
    <li class="two"><span>1</span>Introduction to<br>Harlow Credit Management</li>
    <li class="two"><span>2</span>Investment/Portfolio<br>Management Style</li>
    <li class="one"><span>3</span>Investment Process</li>
    <li class="one"><span>4</span>Business Strategy</li>
    <li class="one"><span>5</span>Operational Excellence</li>
    <li class="one"><span>6</span>Risk Management Capabilities</li>
    <li class="one"><span>7</span>Market Commentary</li>
  </ol>
</section>

<section class="slide s-columns">
  <div class="brand">VALDRIK</div>
  <div class="head-divider"></div>
  <h2 class="head-title">Lorem ipsum dolor sit<br>amet, consectetur adi</h2>
  <article class="col" style="left:11.5px">
    <div class="photo tone-4" role="img" aria-label="Colleagues gathered around a laptop"></div>
    <h3>Lorem ipsum dolor sit amet<br>consectetur adi</h3>
    <p>Sed ut perspiciatis unde omnis iste natus error sit voluptatem accusa ntium doloremque laudantium, totam rem aperiam, eaque ipsa quae ab illo inventore veritatis</p>
  </article>
  <article class="col" style="left:149px">
    <div class="photo tone-5" role="img" aria-label="Two colleagues reviewing a laptop"></div>
    <h3>Lorem ipsum dolor sit amet<br>consectetur adi</h3>
    <p>Sed ut perspiciatis unde omnis iste natus error sit voluptatem accusa ntium doloremque laudantium, totam rem aperiam, eaque ipsa quae ab illo inventore veritatis</p>
  </article>
  <article class="col" style="left:290px">
    <div class="photo tone-6" role="img" aria-label="Team working together in an open office"></div>
    <h3>Lorem ipsum dolor sit amet<br>consectetur adi</h3>
    <p>Sed ut perspiciatis unde omnis iste natus error sit voluptatem accusa ntium doloremque laudantium, totam rem aperiam, eaque ipsa quae ab illo inventore veritatis</p>
  </article>
</section>

<section class="slide s-chart">
  <svg class="chart-art" width="437" height="246" viewBox="0 0 755 424" font-family="Montserrat, sans-serif" font-size="13" fill="#333">
    <g stroke="#23506f" stroke-width="1.4">
      <line x1="98" y1="351" x2="98" y2="372"/>
      <line x1="141" y1="291" x2="141" y2="372"/>
      <line x1="184" y1="260" x2="184" y2="372"/>
      <line x1="228" y1="255" x2="228" y2="372"/>
      <line x1="271" y1="217" x2="271" y2="372"/>
      <line x1="314" y1="236" x2="314" y2="372"/>
      <line x1="357" y1="194" x2="357" y2="372"/>
      <line x1="400" y1="241" x2="400" y2="372"/>
      <line x1="444" y1="200" x2="444" y2="372"/>
      <line x1="487" y1="173" x2="487" y2="372"/>
    </g>
    <line x1="55" y1="115" x2="55" y2="373" stroke="#23506f" stroke-width="4"/>
    <line x1="53" y1="372" x2="528" y2="372" stroke="#23506f" stroke-width="4"/>
    <polyline points="55,372 98,351 141,291 184,260 228,255 271,217 314,236 357,194 400,241 444,200 487,173" fill="none" stroke="#a8894f" stroke-width="3.5" stroke-linejoin="round"/>
    <g text-anchor="end">
      <text x="37" y="165">100</text>
      <text x="37" y="207">80</text>
      <text x="37" y="250">60</text>
      <text x="37" y="292">40</text>
      <text x="37" y="335">20</text>
    </g>
    <g text-anchor="middle">
      <text x="37" y="399">0</text>
      <text x="97" y="399">10</text>
      <text x="141" y="399">20</text>
      <text x="184" y="399">30</text>
      <text x="227" y="399">40</text>
      <text x="270" y="399">50</text>
      <text x="313" y="399">60</text>
      <text x="356" y="399">70</text>
      <text x="399" y="399">80</text>
      <text x="442" y="399">90</text>
      <text x="487" y="399">100</text>
    </g>
  </svg>
  <div class="brand">VALDRIK</div>
  <aside class="chart-panel">
    <h2>Lorem ipsum dolor sit ame consectetur adipiscing elit, sed</h2>
    <p>Sed ut perspiciatis unde omnis iste natus error sit voluptatem accu santium doloremque laudantium, totam rem aperiam, eaque ipsa quae ab illo inventore veritatis et quasi architecto beatae vitae eos qui ratione voluptatem sequi nesciunt. Neque porro quisquam est, qui dolorem ipsum quia dolor sit amet, consectetur, adipisci velit, sed quia non numquam eius modi tempora incidunt ut labore et dolore magnam aliquam quaerat voluptatem. Ut enim ad minima veniam, quis nostrum exercit ationem ullam corporis suscipit laboriosam, nisi ut aliquid ex ea commodi consequatur? Quis autem ve</p>
  </aside>
</section>

<section class="slide s-close">
  <div class="photo" role="img" aria-label="Office workspace, tinted blue" style="inset:0;background:radial-gradient(ellipse at 30% 70%,rgba(15,40,58,.4),rgba(0,0,0,0) 65%)"></div>
  <div class="close-rule" style="top:107px"></div>
  <h2 class="close-title">THANK YOU</h2>
  <div class="close-rule" style="top:150px"></div>
  <div class="contact" style="left:127px">
    <span class="icon"><svg width="8" height="8" viewBox="0 0 24 24"><path fill="#fff" d="M6.6 10.8a15.1 15.1 0 0 0 6.6 6.6l2.2-2.2c.3-.3.7-.4 1-.2 1.1.4 2.3.6 3.6.6.6 0 1 .4 1 1V20c0 .6-.4 1-1 1A17 17 0 0 1 3 4c0-.6.4-1 1-1h3.5c.6 0 1 .4 1 1 0 1.3.2 2.5.6 3.6.1.3 0 .7-.2 1z"/></svg></span>
    <span>Call Us<br>+1 555 010 2040</span>
  </div>
  <div class="contact" style="left:228px">
    <span class="icon"><svg width="8" height="8" viewBox="0 0 24 24"><path fill="#fff" d="M3 5h18v14H3z"/><path fill="none" stroke="#2a2f35" stroke-width="2" d="M3 6l9 7 9-7"/></svg></span>
    <span>Email Us<br>info@valdrik.com</span>
  </div>
</section>

</body>
</html>
```